Business Card Design for Animal Clinic

We are seeking a two sided business card design. The primary side should include our logo (provided in AI and EPS files) address, phone, website, and if possible "Follow Us" with icons for Facebook, Google+, and Twitter.

The back of the card needs to included space for appointment reminders.

Company Name:
Brindlecove Animal Clinic

Doctor Name:
To be provided to winner

Adress:
To be provided to winner

Phone:
to be provided to winner

Website:
www.brindlecoveanimalclinic.example

Industry/Entity Type

Business

```html
<!DOCTYPE html>
<html lang="en">
<head>
<meta charset="utf-8">
<title>Brindlecove Animal Clinic – Business Card</title>
<link href="https://fonts.googleapis.com/css2?family=Noto+Sans:wght@400;500&display=swap" rel="stylesheet">
<style>
  :root {
    --rust: #a6392e;
    --clay: #d4957a;
    --paper: #ffffff;
    --backdrop: #000000;
  }
  html, body {
    margin: 0;
    padding: 0;
    width: 1000px;
    height: 1200px;
    overflow: hidden;
    background: var(--backdrop);
  }
  .card {
    position: absolute;
    left: 76px;
    top: 367px;
    width: 861px;
    height: 503px;
    background: var(--paper);
    font-family: "Noto Sans", Arial, sans-serif;
    color: var(--rust);
    overflow: hidden;
  }
  .band { position: absolute; left: 0; width: 100%; }
  .band--top-dark { top: 0; height: 24px; background: var(--rust); }
  .band--top-light { top: 34px; height: 7px; background: var(--clay); }
  .band--bottom-light { top: 462px; height: 8px; background: var(--clay); }
  .band--bottom-dark { top: 480px; height: 23px; background: var(--rust); }

  .brand {
    position: absolute;
    left: 40px;
    top: 190px;
    width: 380px;
    text-align: center;
    color: var(--rust);
    font-weight: 500;
    margin: 0;
    line-height: 1.15;
  }
  .brand__main { display: block; font-size: 40px; letter-spacing: 1px; }
  .brand__sub { display: block; font-size: 22px; letter-spacing: 2px; margin-top: 8px; }

  .divider {
    position: absolute;
    left: 430px;
    top: 78px;
    width: 2px;
    height: 328px;
    background: var(--rust);
  }

  .doctor-name {
    position: absolute;
    left: 448px;
    top: 143px;
    width: 320px;
    text-align: center;
    font-size: 24px;
    font-weight: 500;
    margin: 0;
  }

  .contact-list {
    position: absolute;
    left: 448px;
    top: 257px;
    margin: 0;
    padding: 0;
    list-style: none;
  }
  .contact-item {
    display: flex;
    align-items: center;
    height: 44px;
    margin-bottom: 8.5px;
    font-size: 18px;
    font-weight: 500;
    white-space: nowrap;
  }
  .contact-icon {
    width: 44px;
    height: 44px;
    background: var(--clay);
    flex: none;
    margin-right: 13px;
  }
  .contact-icon svg { display: block; }
</style>
</head>
<body>
  <div class="card">
    <div class="band band--top-dark"></div>
    <div class="band band--top-light"></div>

    <p class="brand">
      <span class="brand__main">BRINDLECOVE</span>
      <span class="brand__sub">ANIMAL CLINIC</span>
    </p>

    <div class="divider"></div>

    <p class="doctor-name">Doctor Name</p>

    <ul class="contact-list">
      <li class="contact-item">
        <span class="contact-icon">
          <svg width="44" height="44" viewBox="0 0 44 44" aria-hidden="true">
            <path d="M8 22 L22 9 L36 22" fill="none" stroke="#fff" stroke-width="3" stroke-linejoin="round" stroke-linecap="round"/>
            <path d="M13 21 V34 H19 V27 H25 V34 H31 V21" fill="none" stroke="#fff" stroke-width="3" stroke-linejoin="round"/>
          </svg>
        </span>
        <span class="contact-text">14 Harbor Lane, Suite 8</span>
      </li>
      <li class="contact-item">
        <span class="contact-icon">
          <svg width="44" height="44" viewBox="0 0 44 44" aria-hidden="true">
            <path d="M14 9 L19 14 L16 18 C18 23 21 26 26 28 L30 25 L35 30 L31 35 C20 34 10 24 9 13 Z" fill="#fff"/>
          </svg>
        </span>
        <span class="contact-text">555-01234</span>
      </li>
      <li class="contact-item">
        <span class="contact-icon">
          <svg width="44" height="44" viewBox="0 0 44 44" aria-hidden="true">
            <g fill="none" stroke="#fff" stroke-width="2">
              <circle cx="22" cy="22" r="13"/>
              <ellipse cx="22" cy="22" rx="6" ry="13"/>
              <line x1="9" y1="22" x2="35" y2="22"/>
              <line x1="22" y1="9" x2="22" y2="35"/>
              <path d="M11 15 H33 M11 29 H33"/>
            </g>
          </svg>
        </span>
        <span class="contact-text">www.brindlecoveanimalclinic.example</span>
      </li>
    </ul>

    <div class="band band--bottom-light"></div>
    <div class="band band--bottom-dark"></div>
  </div>
</body>
</html>
```